We're a trash valet service. We collect trash that tenants at apartment communitys, elder/assisted liveing would be ideal but we collect Sunday through Thursdays and also offer morning check ups to make sure nothing is left out for pickup. Id like it basic but elegant with little to no cartoon caricatures. But not aposed to them if done right. Colors tequise, orange, blue not married to any of the in spasific.

Porchside Pickup
Number : 555-304-7182
Address: 438 Larkmeadow Road, Suite 2
Fernbrook NJ 08099
Email: Marlene@porchside-pickup.example

I attached my logo.
Those don't have to be the colors plain black is fine for the broshour but I do like those colors with orange maybe.
Updates

Everyone is doing such amazing work. I wanted to just make sure I let everyone know what I need and what should not be on broshour. We do not have garbage trucks, we just both of trash in on site dumpsters or compactors. We use tall kitchen cans for residents to put their garbage in and on in the cans outside of their doors. Pictures of hallways with cans with our logo on it would be good definitely no one's face. What we provide for managers and their benefiting from our service. residents expierance. We also don't have a QR code scanner. And the morning check up is an added service.

Target Market(s)

Apartment communitys

Requirements
Should not have
• Garbage trucks

```html
<!DOCTYPE html>
<html lang="en">
<head>
<meta charset="UTF-8">
<title>Porchside Pickup – Trash Valet Services</title>
<link href="https://fonts.googleapis.com/css2?family=Playfair+Display:wght@700;800&family=Poppins:wght@400;500;600&display=swap" rel="stylesheet">
<style>
:root{
  --teal:#0e9db3;
  --navy:#0c2a57;
  --orange:#f47c20;
  --ink:#111;
  --panel:#f3f3f3;
  --rule:#c9c9c9;
  --white:#fff;
}
*{margin:0;padding:0;box-sizing:border-box}
html,body{width:893px;height:1200px;overflow:hidden;background:var(--teal)}
.flyer{position:relative;width:893px;height:1200px;background:var(--teal);font-family:"Poppins",sans-serif;color:var(--ink)}
.sheet{position:absolute;left:48px;top:35px;width:797px;height:1130px;background:var(--white)}
.abs{position:absolute}
.serif{font-family:"Playfair Display",serif}

.brand{left:76px;top:51px;width:131px;height:130px;display:flex;flex-direction:column;align-items:center;justify-content:center;gap:8px}
.brand-mark{width:40px;height:40px;background:var(--navy)}
.brand-name{font-family:"Poppins",sans-serif;font-weight:600;font-size:13px;line-height:1.15;color:var(--navy);text-align:center}

.title{left:82px;top:213px;font-weight:800;font-size:52px;line-height:52px;color:var(--navy);letter-spacing:-0.5px}
.title-accent{left:82px;top:266px;font-weight:800;font-size:52px;line-height:52px;color:var(--teal);letter-spacing:-0.5px}
.bar{height:3px;width:62px;background:var(--orange)}
.tagline{left:87px;top:354px;width:240px;font-weight:600;font-size:15.5px;line-height:26px;color:var(--ink)}

.photo{left:0;top:0;width:893px;height:1200px;pointer-events:none}

.services-panel{left:48px;top:424px;width:271px;height:499px;background:var(--panel)}
.divider-v{left:331px;top:437px;width:1px;height:512px;background:var(--rule)}
.h2{font-weight:700;font-size:27px;line-height:30px;color:var(--navy)}

.service-icon{width:46px;height:46px;border-radius:50%;display:flex;align-items:center;justify-content:center}
.service-icon.teal{background:var(--teal)}
.service-icon.navy{background:var(--navy)}
.service-icon.orange{background:var(--orange)}
.service-title{font-weight:600;font-size:11.2px;line-height:17px;color:var(--ink)}
.service-text{font-size:8.3px;line-height:14px;color:var(--ink)}

.about-text{left:371px;width:400px;font-size:8.3px;line-height:14.3px;color:var(--ink)}
.rule-h{left:372px;top:697px;width:415px;height:1px;background:var(--rule)}

.step-line{left:391px;top:816px;width:349px;height:5px;background:var(--navy)}
.step-num{width:60px;height:60px;border-radius:50%;display:flex;align-items:center;justify-content:center;color:var(--white);font-weight:600;font-size:31px}
.step-num.navy{background:var(--navy)}
.step-num.teal{background:var(--teal)}
.step-num.orange{background:var(--orange)}
.step-title{font-weight:600;font-size:10.5px;line-height:14px;color:var(--ink)}
.step-text{font-size:8.3px;line-height:14.1px;color:var(--ink);width:90px}

.schedule{left:94px;top:981px;width:461px;height:82px;background:var(--navy);border-radius:6px}
.schedule-label{font-size:11px;font-weight:500;letter-spacing:0.3px}
.schedule-label.orange{color:var(--orange)}
.schedule-label.teal{color:var(--teal)}
.schedule-value{font-size:15.5px;color:var(--white)}
.schedule-divider{left:245px;top:15px;width:1px;height:52px;background:var(--white)}

.promise{left:580px;top:994px;font-weight:700;font-size:15px;line-height:26px;color:var(--ink);letter-spacing:0.2px}

.footer{left:48px;top:1095px;width:797px;height:70px;background:var(--orange)}
.contact-icon{width:33px;height:33px;border-radius:50%;background:var(--navy);display:flex;align-items:center;justify-content:center}
.contact-text{font-weight:600;font-size:13px;line-height:19.5px;color:var(--ink)}
</style>
</head>
<body>
<div class="flyer">
  <div class="sheet"></div>

  <div class="abs brand">
    <div class="brand-mark"></div>
    <div class="brand-name">PORCHSIDE<br>PICKUP LLC</div>
  </div>

  <div class="abs title serif">TRASH VALET</div>
  <div class="abs title-accent serif">SERVICES</div>
  <div class="abs bar" style="left:86px;top:329px"></div>
  <div class="abs tagline">Reliable. Consistent. On Your Doorstep.</div>

  <svg class="abs photo" viewBox="0 0 893 1200">
    <defs>
      <linearGradient id="heroFill" x1="0" y1="0" x2="1" y2="1">
        <stop offset="0" stop-color="#5d6660"/>
        <stop offset="0.45" stop-color="#c98a5a"/>
        <stop offset="0.7" stop-color="#8a8d90"/>
        <stop offset="1" stop-color="#5c6066"/>
      </linearGradient>
    </defs>
    <path role="img" aria-label="Photo of a sanitation worker in orange workwear carrying a trash bag along a paved walkway, seen from behind" d="M845 42 H661 A239 239 0 0 0 661 519 H845 Z" fill="url(#heroFill)"/>
    <path d="M845 84 H658 A197 197 0 0 0 658 478 H845" fill="none" stroke="#fff" stroke-width="1.5"/>
  </svg>

  <div class="abs services-panel"></div>
  <div class="abs divider-v"></div>
  <div class="abs h2 serif" style="left:82px;top:437px">Our Services</div>
  <div class="abs bar" style="left:82px;top:476px"></div>

  <div class="abs service-icon teal" style="left:85px;top:496px">
    <svg width="26" height="26" viewBox="0 0 26 26" fill="none" stroke="#fff" stroke-width="1.1"><rect x="2" y="5" width="20" height="16" rx="2"/><line x1="2" y1="9" x2="22" y2="9"/><line x1="7" y1="3" x2="7" y2="7"/><line x1="17" y1="3" x2="17" y2="7"/><rect x="5" y="12" width="2.5" height="2"/><rect x="10" y="12" width="2.5" height="2"/><rect x="15" y="12" width="2.5" height="2"/><rect x="5" y="16" width="2.5" height="2"/><rect x="10" y="16" width="2.5" height="2"/><circle cx="20" cy="19" r="4" fill="#0e9db3"/><path d="M20 17v2l1.5 1"/></svg>
  </div>
  <div class="abs service-title" style="left:134px;top:497px">SUNDAY – THURSDAY<br>TRASH COLLECTION</div>
  <div class="abs service-text" style="left:134px;top:536px;width:175px">We collect your trash at your doorstep and take it to the community dumpster.</div>

  <div class="abs service-icon navy" style="left:85px;top:592px">
    <svg width="26" height="26" viewBox="0 0 26 26" fill="none" stroke="#fff" stroke-width="1.1"><path d="M6 20h11a3.5 3.5 0 0 0 0-7 5 5 0 0 0-9.5 1A3 3 0 0 0 6 20z"/><circle cx="17" cy="10" r="3.5"/><line x1="17" y1="3" x2="17" y2="4.5"/><line x1="22.5" y1="10" x2="24" y2="10"/><line x1="21" y1="6" x2="22" y2="5"/><line x1="13" y1="6" x2="12" y2="5"/></svg>
  </div>
  <div class="abs service-title" style="left:137px;top:592px">MORNING CHECK UPS</div>
  <div class="abs service-text" style="left:137px;top:615px;width:175px">We check your doorstep each morning to ensure nothing is left out.</div>

  <div class="abs service-icon orange" style="left:85px;top:671px">
    <svg width="26" height="26" viewBox="0 0 26 26" fill="none" stroke="#fff" stroke-width="1.1"><circle cx="13" cy="13" r="10"/><circle cx="13" cy="13" r="6"/><path d="M10.5 13l2 2 3.5-4"/></svg>
  </div>
  <div class="abs service-title" style="left:140px;top:671px">RELIABLE &amp; CONSISTENT</div>
  <div class="abs service-text" style="left:140px;top:694px;width:165px">You can count on us to be there—rain or shine.</div>

  <div class="abs service-icon navy" style="left:85px;top:746px">
    <svg width="26" height="26" viewBox="0 0 26 26" fill="none" stroke="#fff" stroke-width="1.1"><path d="M3 11L13 4l10 7"/><path d="M5 10v12h16V10"/><rect x="10" y="15" width="4" height="7"/><rect x="15.5" y="13" width="3" height="3"/><line x1="3" y1="22" x2="23" y2="22"/></svg>
  </div>
  <div class="abs service-title" style="left:143px;top:747px">TENANT &amp; RESIDENT<br>SATISFACTION</div>
  <div class="abs service-text" style="left:143px;top:786px;width:150px">A cleaner community and happier residents.</div>

  <div class="abs service-icon teal" style="left:85px;top:835px">
    <svg width="26" height="26" viewBox="0 0 26 26" fill="none" stroke="#fff" stroke-width="1.1"><rect x="7" y="4" width="12" height="18"/><rect x="3" y="9" width="4" height="13"/><rect x="19" y="9" width="4" height="13"/><rect x="9" y="7" width="2" height="2"/><rect x="15" y="7" width="2" height="2"/><rect x="9" y="11" width="2" height="2"/><rect x="15" y="11" width="2" height="2"/><rect x="9" y="15" width="2" height="2"/><rect x="15" y="15" width="2" height="2"/><rect x="12" y="18" width="2" height="4"/></svg>
  </div>
  <div class="abs service-title" style="left:146px;top:835px">IDEAL FOR</div>
  <div class="abs service-text" style="left:146px;top:858px;width:160px">Apartment Communities<br>Elder &amp; Assisted Living Facilities</div>

  <div class="abs h2 serif" style="left:371px;top:538px">About Us</div>
  <div class="abs bar" style="left:372px;top:579px"></div>
  <div class="abs about-text" style="top:597px">Porchside Pickup is a professional trash valet service dedicated to creating cleaner, safer, and more convenient communities.</div>
  <div class="abs about-text" style="top:640px">We specialize in removing the hassle of trash day by collecting residents' waste right from their doorstep and ensuring it's properly disposed of—so your property always looks its best.</div>
  <div class="abs rule-h"></div>

  <div class="abs h2 serif" style="left:372px;top:720px">How It Works</div>
  <div class="abs bar" style="left:372px;top:761px"></div>
  <div class="abs step-line"></div>
  <div class="abs step-num navy" style="left:361px;top:789px">1</div>
  <div class="abs step-num teal" style="left:474px;top:789px">2</div>
  <div class="abs step-num orange" style="left:597px;top:789px">3</div>
  <div class="abs step-num navy" style="left:710px;top:789px">4</div>

  <div class="abs step-title" style="left:362px;top:864px">WE COLLECT</div>
  <div class="abs step-text" style="left:362px;top:886px">We pick up the trash from residents' doorsteps Sunday through Thursday.</div>
  <div class="abs step-title" style="left:475px;top:864px">WE TRANSPORT</div>
  <div class="abs step-text" style="left:475px;top:886px;width:95px">Our team transports the waste to the community dumpster.</div>
  <div class="abs step-title" style="left:597px;top:864px">WE CHECK</div>
  <div class="abs step-text" style="left:597px;top:886px;width:80px">Each morning, we check to ensure no trash is left out.</div>
  <div class="abs step-title" style="left:710px;top:864px">YOU RELAX</div>
  <div class="abs step-text" style="left:710px;top:886px;width:95px">Enjoy a cleaner, more organized community without the hassle.</div>

  <div class="abs schedule">
    <svg class="abs" style="left:20px;top:23px" width="40" height="40" viewBox="0 0 40 40" fill="none" stroke="#fff" stroke-width="1.5"><rect x="2" y="5" width="34" height="30" rx="2"/><line x1="2" y1="12" x2="36" y2="12"/><circle cx="9" cy="4" r="2"/><circle cx="19" cy="4" r="2"/><circle cx="29" cy="4" r="2"/><rect x="7" y="16" width="4" height="3.5"/><rect x="14" y="16" width="4" height="3.5"/><rect x="21" y="16" width="4" height="3.5"/><rect x="28" y="16" width="4" height="3.5"/><rect x="7" y="23" width="4" height="3.5"/><rect x="14" y="23" width="4" height="3.5"/><circle cx="31" cy="30" r="7" fill="#0c2a57"/><path d="M28 30l2.3 2.3 4-4.3"/></svg>
    <div class="abs schedule-label orange" style="left:76px;top:21px">SERVICE DAYS:</div>
    <div class="abs schedule-value" style="left:76px;top:42px">Sunday – Thursday</div>
    <div class="abs schedule-divider"></div>
    <div class="abs schedule-label teal" style="left:274px;top:21px">CHECK UPS:</div>
    <div class="abs schedule-value" style="left:274px;top:42px">Every Morning</div>
    <svg class="abs" style="left:406px;top:11px" width="44" height="44" viewBox="0 0 44 44" fill="none" stroke="#fff" stroke-width="1.5"><circle cx="22" cy="22" r="11"/><line x1="22" y1="2" x2="22" y2="7"/><line x1="22" y1="37" x2="22" y2="42"/><line x1="2" y1="22" x2="7" y2="22"/><line x1="37" y1="22" x2="42" y2="22"/><line x1="8" y1="8" x2="11" y2="11"/><line x1="33" y1="33" x2="36" y2="36"/><line x1="36" y1="8" x2="33" y2="11"/><line x1="11" y1="33" x2="8" y2="36"/></svg>
  </div>

  <div class="abs promise serif">DEPENDABLE SERVICE.<br>PROFESSIONAL RESULTS.</div>

  <div class="abs footer"></div>
  <div class="abs contact-icon" style="left:90px;top:1117px">
    <svg width="17" height="17" viewBox="0 0 24 24" fill="none" stroke="#fff" stroke-width="1.6"><path d="M5 3h4l2 5-2.5 1.5a11 11 0 0 0 6 6L16 13l5 2v4a2 2 0 0 1-2 2A16 16 0 0 1 3 5a2 2 0 0 1 2-2z"/></svg>
  </div>
  <div class="abs contact-text" style="left:130px;top:1124px">555-304-7182</div>

  <div class="abs contact-icon" style="left:255px;top:1117px">
    <svg width="17" height="17" viewBox="0 0 24 24" fill="none" stroke="#fff" stroke-width="1.6"><rect x="3" y="6" width="18" height="12"/><path d="M3 6l9 7 9-7"/><path d="M3 18l7-6M21 18l-7-6"/></svg>
  </div>
  <div class="abs contact-text" style="left:292px;top:1124px;font-size:12.4px">Marlene@porchside-pickup.example</div>

  <div class="abs contact-icon" style="left:547px;top:1117px">
    <svg width="17" height="17" viewBox="0 0 24 24" fill="none" stroke="#fff" stroke-width="1.6"><path d="M12 22s7-7 7-12a7 7 0 0 0-14 0c0 5 7 12 7 12z"/><circle cx="12" cy="10" r="2.5"/></svg>
  </div>
  <div class="abs contact-text" style="left:587px;top:1117px">438 Larkmeadow Road, Suite 2,<br>Fernbrook NJ 08099</div>
</div>
</body>
</html>
```